PetalDrops - promoting myself as an aromatherapist, VeloMira Wellness Advocate and as Ask Corinna (

This is my first time requesting a web design, so please be patient with me and let me know if you need anything else.
I have a logo which I love and want to use. I've loaded up 3 different file formats, please tell me if you want a different format. I also have web space with web address attached and Wordpress is loaded - www.petaldrops.com.au
I'm frustrated because I don't know how to use WP to the degree I want, but know enough how to add pages, load articles and pictures.
I'm not sure how many pages I need designed. The home page is important. Setting up links is also important. I believe once the overall design is set I can do the rest.
I put 5+ simply because I don't know. Like I said, I know how to add pages. I guess once the overall layout is designed the rest will be easy??
I'd like a home page that has my blog articles with links to the full article. (I've only just begun writing for this)
An information page about veloMIRA and myself (I've begun writing this). A sign up page or link - veloMIRA allocates a personal link for sign up and shopping - mine is www.myvelomira.com/corinna - I have found that people have difficulty finding the 'join and save' button on that page (I find that's a clumsy title), and on my FB page my sign up button goes straight to the sign up page. My FB page is about to change to PetalDrops by Corinna. A link to this on the web site.
A contact me page.
I do articles for essential oils. Plus I also want a Ask Corinna blog. Ask Corinna is similar to Hey Marla. I'm not sure if this should be a separate website or if it can be incorporated into PetalDrops as there IS overlap. I would like to incorporate both.
I have learnt that when people Google veloMIRA in Australia they get US signup pages without realising it. I cannot put veloMIRA Australia on my webpage, but I can put Go Essential Oils Australia or veloMIRA by Corinna in Australia or similar. veloMIRA have strict rules about compliance, but do allow people their own websites.
I want a slick, engaging, user friendly, easily navigated site.
I will update this description as I see ideas come in and understand more of what I want.
I am going to be direct with people as I don't want to waste anyone's time and I don't want anyone to waste mine.
If you don't read this brief don't bother submitting designs.
Please talk to me, I found someone for my logo design who worked with me and as a result we got exactly what I wanted before the due date.
I'm also working on getting a better photo of myself to use. I've also uploaded a couple of documents, unfinished, but enough to get going (I hope!).

Target Market(s)

men, women, mums with bubs/children

Industry/Entity Type

Wellness

Number of Pages Required

5+ page

Requirements
Must have
• Colours are very important and specific - violet.
• Easily navigated.
• Blog and other pages.
Nice to have
• other colours - ice blue, pale yellow, pale pink, royal blue, medium green (think fertilised grass), silver, gold
Should not have
• grey, black

```html
<!DOCTYPE html>
<html lang="en">
<head>
<meta charset="utf-8">
<title>PetalDrops by Corinna</title>
<link rel="stylesheet" href="https://fonts.googleapis.com/css2?family=Montserrat:wght@400;600;700&family=Open+Sans:wght@400;600&display=swap">
<style>
:root{
  --violet:#6b2d96;
  --violet-soft:#9b59c4;
  --violet-pale:#c9a6e0;
  --page:#f4f3f6;
  --card:#ffffff;
  --ink:#2e2a33;
  --muted:#77727c;
  --rule:#e4e1e8;
  --footer:#ecebee;
}
*{box-sizing:border-box;margin:0;padding:0}
html,body{width:1200px;height:2554px;overflow:hidden}
body{background:var(--page);font-family:"Open Sans",Arial,sans-serif;color:var(--ink);position:relative}
.abs{position:absolute}
h1,h2,h3,h4,.nav,.btn,.label{font-family:"Montserrat",Arial,sans-serif}

/* top bar */
.topbar{left:0;top:0;width:1200px;height:32px;background:#fff;border-bottom:1px solid var(--rule)}
.topbar .inner{position:absolute;left:234px;width:732px;top:0;height:32px;display:flex;align-items:center;gap:14px;font-size:9.5px}
.nav a{color:var(--ink);text-decoration:none;margin-right:10px}
.nav .submit{font-weight:700;margin-right:18px}
.socials{margin-left:auto;display:flex;gap:9px}
.dot{width:10px;height:10px;border-radius:50%;background:var(--muted);display:inline-block}

/* brand */
.brand{left:0;width:1200px;top:48px;text-align:center}
.brand .name{font-family:"Montserrat",sans-serif;font-weight:600;font-size:56px;color:var(--violet);letter-spacing:1px;display:inline-flex;align-items:center;gap:14px}
.brand .mark{width:22px;height:22px;border-radius:50%;background:var(--violet-soft)}
.brand .by{font-family:"Montserrat",sans-serif;font-size:13px;letter-spacing:6px;color:var(--muted);margin-top:2px}

/* hero */
.hero{left:234px;top:150px;width:732px;height:305px;background:linear-gradient(180deg,#b9c98a 0%,#8aa24b 45%,#4f7a22 100%)}
.hero .caption{position:absolute;left:30px;bottom:38px;color:#fff;width:440px}
.hero h2{font-size:16px;font-weight:700;margin-bottom:6px}
.hero p{font-size:14.5px;line-height:1.35}
.tabs{left:234px;top:458px;width:732px;display:flex;justify-content:space-between;font-size:8.5px}
.tabs .tab{width:200px;border-bottom:2px solid var(--violet);padding-bottom:4px}
.tabs b{color:var(--violet);margin-right:8px}

/* instagram strip */
.strip{left:234px;top:498px;width:732px;height:126px;display:flex;background:#fff}
.strip .ph{flex:1;height:100%}
.strip .tag{position:absolute;left:316px;top:-8px;background:var(--violet);color:#fff;font-size:8.5px;padding:3px 12px;font-family:"Montserrat",sans-serif}
.strip .arrow{position:absolute;top:52px;color:#fff;font-size:16px}

/* section head */
.sechead{font-size:13px;font-weight:700;letter-spacing:1px}
.sechead::after{content:"";display:block;width:60px;height:2px;background:var(--violet);margin-top:6px}

/* cards */
.card{background:var(--card);position:absolute}
.card .img{width:100%}
.card h3{font-size:11.5px;font-weight:600;letter-spacing:.6px;text-transform:uppercase}
.meta{font-size:8px;color:var(--muted);margin-top:5px;font-family:"Montserrat",sans-serif}
.meta b{color:var(--violet)}
.line{width:110px;height:1px;background:var(--violet-soft);margin:10px 0 12px}
.card p{font-size:9.5px;line-height:1.6;color:var(--muted)}
.btn{display:inline-block;background:var(--violet);color:#fff;font-size:8px;font-weight:600;padding:7px 13px;letter-spacing:.4px}
.btn.ghost{background:#fff;color:var(--ink);border:1px solid var(--rule)}
.share{display:flex;gap:6px;align-items:center}
.share i{width:22px;height:22px;border:1px solid var(--rule);display:flex;align-items:center;justify-content:center}
.share i span{width:7px;height:7px;border-radius:50%;background:var(--muted)}
.share .go{width:22px;height:22px;background:var(--violet);display:flex;align-items:center;justify-content:center}
.row{display:flex;justify-content:space-between;align-items:center}
.badge{position:absolute;left:8px;top:8px;width:20px;height:16px;background:var(--violet)}

/* sidebar */
.side{background:#fff;position:absolute;left:794px;width:172px;padding:14px 12px}
.side h4{font-size:10.5px;font-weight:700;letter-spacing:.8px}
.side h4::after{content:"";display:block;width:50px;height:2px;background:var(--violet);margin-top:6px}
.pop{display:flex;gap:8px;margin-top:14px}
.pop .th{width:44px;height:32px;flex:none}
.pop h5{font-family:"Montserrat",sans-serif;font-size:8px;font-weight:600}
.pop small{font-size:7px;color:var(--muted)}
.cats li{list-style:none;font-size:8px;font-family:"Montserrat",sans-serif;padding:8px 0;border-bottom:1px solid var(--rule)}

/* footer */
.footer{left:0;top:2169px;width:1200px;height:333px;background:var(--footer);border-top:3px solid var(--violet)}
.footer h4{font-size:10.5px;font-weight:700;letter-spacing:.8px}
.footer h4::after{content:"";display:block;width:50px;height:2px;background:var(--violet);margin-top:6px}
.fcol{position:absolute;top:40px;font-size:8.5px;line-height:1.6;color:var(--muted)}
.fcol input{display:block;width:232px;height:28px;border:1px solid var(--rule);background:#fff;font-size:8px;padding:0 8px;margin-top:8px;font-family:"Open Sans",sans-serif}
.up{left:942px;top:2160px;width:22px;height:22px;background:var(--violet)}
</style>
</head>
<body>

<header class="topbar abs">
  <div class="inner nav">
    <svg width="12" height="12" viewBox="0 0 12 12" aria-hidden="true"><circle cx="5" cy="5" r="3.6" fill="none" stroke="#2e2a33" stroke-width="1.5"/><line x1="7.8" y1="7.8" x2="11" y2="11" stroke="#2e2a33" stroke-width="1.5"/></svg>
    <div>
      <a class="submit">SUBMIT STORY</a><a>Home</a><a>About</a><a>Wellbeing Consults</a><a>Essential Oils</a><a>Events</a><a>FAQ</a><a>Contact us</a><a>Feedback</a><a>Blog</a>
    </div>
    <div class="socials" aria-label="Social links"><span class="dot"></span><span class="dot"></span><span class="dot"></span><span class="dot"></span><span class="dot"></span><span class="dot"></span></div>
  </div>
</header>

<div class="brand abs">
  <div class="name"><span>PetalDrops</span><span class="mark"></span></div>
  <div class="by">by Corinna</div>
</div>

<section class="hero abs" role="img" aria-label="Photo of Corinna standing in a green grassy field with arms outstretched">
  <div class="caption">
    <h2>Hello, I'm Corinna</h2>
    <p>I'm an Aromatherapist, veloMIRA Wellness Advocate and Wellness Consultant. I'm passionate about health and wellbeing and want to help you help yourself.</p>
  </div>
</section>

<div class="tabs abs label">
  <div class="tab"><b>01.</b>ENJOY LIFE STYLE</div>
  <div class="tab"><b>02.</b>HEALTH</div>
  <div class="tab"><b>03.</b>WELLNESS</div>
</div>

<section class="strip abs" aria-label="Instagram feed">
  <div class="ph" role="img" aria-label="Oil bottles diagram" style="background:linear-gradient(#e9e4ee,#cfc3dc)"></div>
  <div class="ph" role="img" aria-label="Portrait photo" style="background:linear-gradient(#d8cfc0,#b7a68e)"></div>
  <div class="ph" role="img" aria-label="Orange blossom and oranges" style="background:linear-gradient(#6f8c3a,#e38b1c)"></div>
  <div class="ph" role="img" aria-label="Cartoon hero graphic" style="background:linear-gradient(#f3eee6,#c9322a)"></div>
  <div class="ph" role="img" aria-label="Oil bottles on a table" style="background:linear-gradient(#e7e2ea,#8a7290)"></div>
  <span class="tag">INSTAGRAM</span>
  <span class="arrow" style="left:6px">‹</span><span class="arrow" style="right:6px;color:var(--ink)">›</span>
</section>

<h2 class="sechead abs" style="left:234px;top:660px">RECENT POST</h2>

<!-- featured post -->
<article class="card" style="left:234px;top:700px;width:544px;height:434px">
  <div class="img" role="img" aria-label="Lavender field with an oil bottle" style="height:230px;background:linear-gradient(100deg,#5a3d74 0%,#9b6bc9 40%,#b48ad8 70%,#7d8e4c 100%)"></div>
  <span class="badge"></span>
  <div style="padding:20px 20px 0">
    <h3>Exploring Healthy Life</h3>
    <div class="meta">BY <b>MARA QUILL</b> &nbsp; SEPTEMBER 17, 2015</div>
    <div class="line"></div>
    <p>Small daily rituals shape how we feel. A few drops of lavender at bedtime, a walk in fresh air and a glass of water on waking can change the tone of a whole day. In this post I share the simple routines that help my family rest well, stay calm and keep our energy steady through busy weeks.</p>
    <div class="row" style="margin-top:18px">
      <span class="btn">CONTINUE READING</span>
      <div class="share"><i><span></span></i><i><span></span></i><i><span></span></i><i><span></span></i><span class="go"><svg width="9" height="9" viewBox="0 0 9 9"><circle cx="7" cy="1.8" r="1.3" fill="#fff"/><circle cx="1.8" cy="4.5" r="1.3" fill="#fff"/><circle cx="7" cy="7.2" r="1.3" fill="#fff"/><path d="M7 1.8 1.8 4.5 7 7.2" stroke="#fff" fill="none" stroke-width=".8"/></svg></span></div>
    </div>
  </div>
</article>

<!-- two column posts -->
<article class="card" style="left:234px;top:1159px;width:262px;height:349px">
  <div class="img" role="img" aria-label="City buildings photo" style="height:149px;background:linear-gradient(#c8d4e2,#7f8a93)"></div>
  <span class="badge"></span>
  <div style="padding:18px 14px 0">
    <h3>Girl Fashion Lifestyle</h3>
    <div class="meta">BY <b>MARA QUILL</b> &nbsp; SEPTEMBER 17, 2015</div>
    <div class="line"></div>
    <p>A gentle morning blend for busy mums. Mix citrus and mint to lift the mood and start the day clear.</p>
    <div class="row" style="margin-top:16px"><span class="btn ghost">READ MORE</span><div class="share"><i style="border:0"><span></span></i><i style="border:0"><span></span></i><i style="border:0"><span></span></i><span class="go"></span></div></div>
  </div>
</article>
<article class="card" style="left:514px;top:1159px;width:264px;height:349px">
  <div class="img" role="img" aria-label="Cloves and lemongrass with diffuser tip text" style="height:149px;background:linear-gradient(#9a6a3a,#4a2a15)"></div>
  <span class="badge"></span>
  <div style="padding:18px 14px 0">
    <h3>Girl Fashion Lifestyle</h3>
    <div class="meta">BY <b>MARA QUILL</b> &nbsp; SEPTEMBER 17, 2015</div>
    <div class="line"></div>
    <p>Clove and lemongrass in the diffuser help keep the home fresh and support the body in cold season.</p>
    <div class="row" style="margin-top:16px"><span class="btn ghost">READ MORE</span><div class="share"><i style="border:0"><span></span></i><i style="border:0"><span></span></i><i style="border:0"><span></span></i><span class="go"></span></div></div>
  </div>
</article>

<!-- list posts -->
<article class="card" style="left:234px;top:1522px;width:544px;height:178px">
  <div class="abs" role="img" aria-label="Two for one oil offer graphic" style="left:0;top:0;width:188px;height:178px;background:linear-gradient(#e3d3ee,#8a5bb0)"></div>
  <div class="abs" style="left:208px;top:18px;width:318px">
    <h3>Exploring San Francisco's Cuisine</h3>
    <div class="meta">BY <b>MARA QUILL</b> &nbsp; SEPTEMBER 17, 2015</div>
    <div class="line"></div>
    <p>Cooking with oils adds bright flavour. A drop of basil or lemon lifts a simple meal for the whole family.</p>
    <div class="row" style="margin-top:14px"><span class="btn">CONTINUE READING</span><div class="share"><i><span></span></i><i><span></span></i><i><span></span></i><i><span></span></i><span class="go"></span></div></div>
  </div>
</article>
<article class="card" style="left:234px;top:1714px;width:544px;height:179px">
  <div class="abs" role="img" aria-label="Oil roller bottles on a green cloth" style="left:0;top:0;width:188px;height:179px;background:linear-gradient(#7aa26a,#3d2a4a)"></div>
  <div class="abs" style="left:208px;top:18px;width:318px">
    <h3>Exploring San Francisco's Cuisine</h3>
    <div class="meta">BY <b>MARA QUILL</b> &nbsp; SEPTEMBER 17, 2015</div>
    <div class="line"></div>
    <p>Roller blends are easy to carry. Keep one in your bag for calm moments and fresh focus on the go.</p>
    <div class="row" style="margin-top:14px"><span class="btn">CONTINUE READING</span><span class="go" style="width:22px;height:22px;background:var(--violet)"></span></div>
  </div>
</article>
<article class="card" style="left:234px;top:1907px;width:544px;height:181px">
  <div class="abs" role="img" aria-label="Strawberry ice cream with text" style="left:0;top:0;width:188px;height:181px;background:linear-gradient(#f6c9cf,#e0566a)"></div>
  <div class="abs" style="left:208px;top:18px;width:318px">
    <h3>You Create Your Opportunities by Asking for Them</h3>
    <div class="meta">BY <b>MARA QUILL</b> &nbsp; SEPTEMBER 17, 2015</div>
    <div class="line"></div>
    <p>Ask Corinna answers your questions each week. Send yours in and let us find the right path together.</p>
    <div class="row" style="margin-top:14px"><span class="btn">CONTINUE READING</span><span class="go" style="width:22px;height:22px;background:var(--violet)"></span></div>
  </div>
</article>

<!-- sidebar -->
<aside class="side" style="top:700px;height:38px;padding:0 10px;display:flex;align-items:center;justify-content:space-between;font-size:8px;color:var(--muted)">
  <span>SEARCH</span>
  <svg width="10" height="10" viewBox="0 0 12 12" aria-hidden="true"><circle cx="5" cy="5" r="3.6" fill="none" stroke="#2e2a33" stroke-width="1.6"/><line x1="7.8" y1="7.8" x2="11" y2="11" stroke="#2e2a33" stroke-width="1.6"/></svg>
</aside>

<aside class="side" style="top:752px;height:270px">
  <h4>POPULAR POST</h4>
  <div class="pop"><div class="th" role="img" aria-label="Thumbnail" style="background:#8a6a4a"></div><div><h5>BEAUTY FASHION</h5><small>SEP. 28 2015</small></div></div>
  <div class="pop"><div class="th" role="img" aria-label="Thumbnail" style="background:#6f8c3a"></div><div><h5>WELLNESS PLAN</h5><small>SEP. 28 2015</small></div></div>
  <div class="pop"><div class="th" role="img" aria-label="Thumbnail" style="background:#a9c48f"></div><div><h5>TRAVEL PLANS</h5><small>SEP. 28 2015</small></div></div>
  <div class="pop"><div class="th" role="img" aria-label="Thumbnail" style="background:#5a4a6a"></div><div><h5>HEALTH TIPS</h5><small>SEP. 28 2015</small></div></div>
</aside>

<aside class="side" style="top:1058px;height:250px">
  <h4>CATAGORIES</h4>
  <ul class="cats" style="margin-top:8px">
    <li>HEALTH (28)</li><li>IMAGES (95)</li><li>WELLNESS (85)</li><li>BEAUTY (145)</li><li>LIFESTYLE (58)</li><li>FOOD (69)</li>
  </ul>
</aside>

<aside class="side" style="top:1316px;height:200px">
  <h4>INSTAGRAM</h4>
  <div style="display:grid;grid-template-columns:repeat(4,1fr);gap:2px;margin-top:16px;width:104px">
    <div role="img" aria-label="Feed image" style="height:25px;background:#8a5bb0"></div>
    <div role="img" aria-label="Feed image" style="height:25px;background:#c94a5a"></div>
    <div role="img" aria-label="Feed image" style="height:25px;background:#5d7a3a"></div>
    <div role="img" aria-label="Feed image" style="height:25px;background:#e39a2a"></div>
    <div role="img" aria-label="Feed image" style="height:25px;background:#9a7ab8"></div>
    <div role="img" aria-label="Feed image" style="height:25px;background:#5a4a6a"></div>
    <div role="img" aria-label="Feed image" style="height:25px;background:#d8c9b0"></div>
    <div role="img" aria-label="Feed image" style="height:25px;background:#b7507a"></div>
  </div>
</aside>

<div class="abs" role="img" aria-label="Coupon 30% promotional banner" style="left:794px;top:1535px;width:172px;height:152px;background:linear-gradient(#3a2a44,#2a1f33);color:#fff;font-family:Montserrat,sans-serif;text-align:center;padding-top:56px">
  <div style="font-size:17px;font-weight:700">COUPON<br>30%</div>
  <span style="display:inline-block;margin-top:8px;background:var(--violet);font-size:6px;padding:3px 8px">LEARN MORE</span>
</div>

<aside class="side" style="top:1704px;height:112px">
  <h4>SOCIAL MEDIA</h4>
  <div class="share" style="margin-top:20px;gap:8px"><i style="border:0"><span></span></i><i style="border:0"><span></span></i><i style="border:0"><span></span></i><i style="border:0"><span></span></i><i style="border:0"><span></span></i><span class="go"></span></div>
</aside>

<aside class="side" style="top:1824px;height:174px">
  <h4>POST SLIDER</h4>
  <div role="img" aria-label="Oil bottle photo slide" style="margin-top:14px;height:106px;background:linear-gradient(#b8a99a,#4e3a2a);position:relative">
    <span style="position:absolute;left:6px;top:42px;width:14px;height:14px;border-radius:50%;background:var(--violet)"></span>
    <span style="position:absolute;right:6px;top:42px;width:14px;height:14px;border-radius:50%;background:var(--violet)"></span>
  </div>
</aside>

<!-- footer -->
<footer class="footer abs">
  <div class="fcol" style="left:234px;width:232px">
    <h4 style="color:var(--ink)">ABOUT ME</h4>
    <p style="margin-top:14px">Hello, I'm Corinna<br>I'm an Aromatherapist, veloMIRA Wellness Advocate and Wellness Consultant.</p>
    <div role="img" aria-label="Portrait photo of Corinna outdoors" style="margin-top:10px;width:232px;height:126px;background:linear-gradient(#c7d8e8,#9aa86e)"></div>
    <div class="btn" style="display:block;text-align:center;margin-top:7px">READ MORE ABOUT ME</div>
  </div>
  <div class="fcol" style="left:482px;width:232px">
    <h4 style="color:var(--ink)">LATEST TWEET</h4>
    <p style="margin-top:14px"><b style="color:var(--ink);font-size:8px">TOBIN HARLOW</b><br>Lovely to hear from readers this week. Your stories about oils at home make this blog a joy to write.<br><span style="color:var(--violet)">@petaldrops_help</span></p>
    <p style="margin-top:16px"><b style="color:var(--ink);font-size:8px">ILSA RENWICK</b><br>New post up on calm bedtime blends for little ones. Share it with a friend who needs rest.<br><span style="color:var(--violet)">@petaldrops_help</span></p>
  </div>
  <div class="fcol" style="left:734px;width:232px">
    <h4 style="color:var(--ink)">SUBSCRIBED &amp; NEWSLETTER</h4>
    <p style="margin-top:14px">Join the list for new posts, wellness tips and seasonal blends sent gently to your inbox.</p>
    <input value="YOUR NAME" aria-label="Your name">
    <input value="YOUR EMAIL ADDRESS" aria-label="Your email address">
    <div class="btn" style="display:block;text-align:center;margin-top:8px;width:232px">SUBSCRIBED NOW</div>
    <p style="margin-top:10px">© Copyright 2016</p>
  </div>
</footer>
<div class="up abs"><svg width="22" height="22" viewBox="0 0 22 22"><path d="M7 13 11 9 15 13" stroke="#fff" stroke-width="1.6" fill="none"/></svg></div>

</body>
</html>
```